Searching for a captivating trade show banner design that captures the audience's attention.

I am looking to have someone design pop up trade show banner to go with my business card and flyer. Must be high resolution to print larger. See attached pics

I extended the timelines on this project.

Target Market(s)

Any commercial facility that would have fitness equipment. Park and Recreation, Fitness Centers, Multi-family, schools

Industry/Entity Type

Fitness space design and planning. fitness equipment sales. High end clients

Colors
0054AA
0677BA
7BADD7
CADEEF
E8F1F8

Requirements
Must have
• Similar look to attached business card and flyer. I would like to try and get custom look to brand. Unique cool design. I do high end facility so some type of architecture elements and or look.
Nice to have
• the smaller logo like the back of my business card somewhere on the banner design
Should not have
• clutter, dark and hard to read

```html
<!DOCTYPE html>
<html lang="en">
<head>
<meta charset="utf-8">
<title>Formwork Fitness – Roll-up Banner</title>
<link rel="stylesheet" href="https://fonts.googleapis.com/css2?family=Montserrat:wght@400;500;700;800&display=swap">
<style>
  :root {
    --page-bg: #ebebeb;
    --blue-deep: #2a55a6;
    --blue-mid: #2f78c2;
    --blue-light: #3a9ad8;
    --brand-cyan: #0096dc;
    --accent: #2aa8ea;
    --ring: #0d62b3;
    --white: #ffffff;
    --ink: #2d2d33;
  }
  * { margin: 0; padding: 0; box-sizing: border-box; }
  html, body { width: 1155px; height: 1200px; overflow: hidden; background: var(--page-bg); }
  body { font-family: "Montserrat", sans-serif; position: relative; }

  .banner {
    position: absolute; left: 312px; top: 40px; width: 531px; height: 1120px;
    overflow: hidden;
    background: linear-gradient(90deg, var(--blue-deep) 0%, var(--blue-deep) 48%, var(--blue-mid) 75%, var(--blue-light) 100%);
  }

  .corner-texture {
    position: absolute; left: 248px; top: 6px; width: 283px; height: 120px;
    background: linear-gradient(90deg, rgba(255,255,255,0) 0%, rgba(190,215,240,0.18) 55%, rgba(200,225,245,0.28) 100%);
  }

  .contact-name {
    position: absolute; left: 42px; top: 160px;
    color: var(--white); font-weight: 400; font-size: 43px; letter-spacing: 0.5px; line-height: 1.1;
  }
  .contact-role {
    position: absolute; left: 45px; top: 205px;
    color: var(--accent); font-weight: 500; font-size: 21px; letter-spacing: 0.5px;
  }
  .contact-list {
    position: absolute; left: 42px; top: 264px; list-style: none;
    color: var(--white); font-size: 23px; font-weight: 400;
  }
  .contact-list li { display: flex; align-items: center; height: 38px; }
  .contact-list svg { width: 18px; height: 18px; margin-right: 18px; flex: none; }

  .photo-ring { position: absolute; border-radius: 50%; }
  .photo-ring.halo { left: 37px; top: 435px; width: 194px; height: 194px; background: rgba(40, 80, 160, 0.5); }
  .photo-ring.solid { left: 36px; top: 627px; width: 196px; height: 196px; background: var(--ring); }
  .photo { position: absolute; width: 160px; height: 160px; border-radius: 50%; }
  .photo.building { left: 54px; top: 452px; background: linear-gradient(170deg, #8c98a8 0%, #7a4e36 45%, #4b3a2c 80%, #4f6b3a 100%); }
  .photo.floorplan { left: 54px; top: 645px; background: radial-gradient(circle at 50% 50%, #c9c4bd 0%, #bdb7ae 55%, #ffffff 72%); }

  .brand-name {
    position: absolute; left: 0; top: 940px; width: 528px; text-align: center;
    color: var(--brand-cyan); font-weight: 800; font-size: 30px; letter-spacing: 1px; line-height: 1;
  }

  .vertical-wordmark {
    position: absolute; left: 472px; top: 572px;
    transform: translate(-50%, -50%) rotate(-90deg);
    white-space: nowrap; color: var(--ink);
    font-weight: 800; font-size: 66px; letter-spacing: 1px; line-height: 1;
  }

  .url-band {
    position: absolute; left: 10px; right: 0; top: 1056px; height: 41px;
    background: linear-gradient(90deg, rgba(255,255,255,0) 0%, rgba(120,190,240,0.35) 45%, #5db4e8 100%);
    display: flex; align-items: center;
  }
  .url-band span { margin-left: 88px; color: var(--white); font-size: 23px; font-weight: 400; }
</style>
</head>
<body>
  <main class="banner">
    <div class="corner-texture" role="img" aria-label="Faded repeating brand pattern"></div>

    <h1 class="contact-name">DANA KESLER</h1>
    <p class="contact-role">PRINCIPAL</p>

    <ul class="contact-list">
      <li>
        <svg viewBox="0 0 24 24" aria-hidden="true"><path fill="#2aa8ea" d="M6.6 10.8a15.1 15.1 0 0 0 6.6 6.6l2.2-2.2c.3-.3.7-.4 1-.2 1.1.4 2.3.6 3.6.6.6 0 1 .4 1 1V20c0 .6-.4 1-1 1A17 17 0 0 1 3 4c0-.6.4-1 1-1h3.5c.6 0 1 .4 1 1 0 1.3.2 2.5.6 3.6.1.3 0 .7-.2 1z"/></svg>
        <span>555 214 0187</span>
      </li>
      <li>
        <svg viewBox="0 0 24 24" aria-hidden="true"><rect x="2" y="5" width="20" height="14" fill="#2aa8ea"/><path d="M2 5l10 8 10-8" fill="none" stroke="#2a55a6" stroke-width="1.6"/></svg>
        <span>Dana@formworkfitness.co</span>
      </li>
      <li>
        <svg viewBox="0 0 24 24" aria-hidden="true"><rect x="3" y="3" width="18" height="18" fill="#2aa8ea"/></svg>
        <span>/danakesler</span>
      </li>
    </ul>

    <div class="photo-ring halo"></div>
    <div class="photo building" role="img" aria-label="Photo of a modern brick multi-storey building with a landscaped courtyard"></div>

    <div class="photo-ring solid"></div>
    <div class="photo floorplan" role="img" aria-label="3D floor plan rendering of a fitness facility layout with equipment zones"></div>

    <p class="brand-name">FORMWORK</p>

    <div class="vertical-wordmark">FORMWORK FITNESS</div>

    <div class="url-band"><span>www.formworkfitness.co</span></div>
  </main>
</body>
</html>
```